Business Card for Managing Partner Investment Fund

To create a business card template for an investment fund manager. Business card should be more professional in nature, not too colorful, more upscale, and created using the attached logos and fund name files. I would prefer a black or gray color scheme, but am open to the use of color as well. I would prefer a double sided business card, but open to single sided business card designs as well. The business card should include: name, title, and contact information, as well as logo and company name. I would prefer a more stream-lined, simple business card design.
Updates
Address: 4190 NE 38th Ter. Larkfield, OR 97318
Email: talvin47@quorimail.net
Phone: 738-347-9162
Title: managing partner
Name: Dorian Velsky
Fund Name: Ambergate Capital
Logos can be found in files attached to the brief
Target Market(s)
potential investors, other fund managers
Industry/Entity Type
Finance
Contact Information for Business Card
Name on card: Dorian Velsky
Title: Managing Partner
Colors
Designer to choose colors to be used in the design.
Requirements
Must have
- Phone number
- email address
- physical address
- title
- name
- logo
- Fund name
Nice to have
- simple layout
Should not have
- too many colors, busy fonts,

```html
<!DOCTYPE html>
<html lang="en">
<head>
<meta charset="utf-8">
<title>Ambergate Capital – Business Card</title>
<link rel="stylesheet" href="https://fonts.googleapis.com/css2?family=Roboto:wght@400;700&display=swap">
<style>
  :root {
    --backdrop: #2b1b15;
    --card-black: #050708;
    --ink-light: #e6e6e6;
    --ink-muted: #c9c9c9;
    --accent-blue: #0f78c4;
    --accent-gray: #c8c8c8;
  }
  * { margin: 0; padding: 0; box-sizing: border-box; }
  html, body {
    width: 1200px; height: 1000px; overflow: hidden;
    background: var(--backdrop);
    font-family: "Roboto", Arial, sans-serif;
  }
  .card {
    position: absolute;
    left: 350px;
    width: 500px; height: 286px;
    background: var(--card-black);
    overflow: hidden;
    box-shadow: 0 6px 18px rgba(0,0,0,.45);
  }
  .card--front { top: 175px; }
  .card--back  { top: 540px; }

  .brand-name {
    position: absolute;
    color: var(--ink-muted);
    font-weight: 400;
    text-transform: uppercase;
    letter-spacing: 2px;
    text-align: center;
    line-height: 1.15;
  }
  .card--front .brand-name { left: 30px; top: 110px; width: 200px; font-size: 24px; }
  .card--back .brand-name {
    left: 0; right: 0; top: 112px; font-size: 38px; letter-spacing: 5px;
  }

  .holder { position: absolute; left: 262px; top: 44px; }
  .holder__name { color: var(--ink-light); font-weight: 700; font-size: 22px; }
  .holder__title { color: var(--ink-muted); font-size: 12px; margin-top: 1px; }

  .contact { position: absolute; left: 280px; top: 104px; list-style: none; }
  .contact__item {
    display: flex; align-items: flex-start; gap: 7px;
    color: var(--ink-muted); font-size: 12px; line-height: 16px; margin-bottom: 4px;
  }
  .contact__icon { width: 11px; height: 11px; margin-top: 2px; flex: none; fill: var(--ink-muted); }

  .card__bands { position: absolute; left: 0; bottom: 0; width: 500px; height: 40px; }
</style>
</head>
<body>

<section class="card card--front" aria-label="Business card front">
  <div class="brand-name">Ambergate<br>Capital</div>

  <div class="holder">
    <div class="holder__name">Dorian Velsky</div>
    <div class="holder__title">Managing Partner</div>
  </div>

  <ul class="contact">
    <li class="contact__item">
      <svg class="contact__icon" viewBox="0 0 24 24"><path d="M6.6 10.8a15.1 15.1 0 0 0 6.6 6.6l2.2-2.2a1 1 0 0 1 1-.25 11.4 11.4 0 0 0 3.6.57 1 1 0 0 1 1 1V20a1 1 0 0 1-1 1A17 17 0 0 1 3 4a1 1 0 0 1 1-1h3.5a1 1 0 0 1 1 1c0 1.25.2 2.45.57 3.57a1 1 0 0 1-.25 1z"/></svg>
      738-347-9162
    </li>
    <li class="contact__item">
      <svg class="contact__icon" viewBox="0 0 24 24"><rect x="2" y="5" width="20" height="14"/><path d="M3 6.5l9 7 9-7" fill="none" stroke="#050708" stroke-width="2"/></svg>
      talvin47@quorimail.net
    </li>
    <li class="contact__item">
      <svg class="contact__icon" viewBox="0 0 24 24"><path d="M12 2a7 7 0 0 0-7 7c0 5.2 7 13 7 13s7-7.8 7-13a7 7 0 0 0-7-7zm0 9.5A2.5 2.5 0 1 1 12 6.5a2.5 2.5 0 0 1 0 5z"/></svg>
      <span>4190 NE 38th Ter.<br>Larkfield, OR 97318</span>
    </li>
  </ul>

  <svg class="card__bands" viewBox="0 0 500 40" aria-hidden="true">
    <rect fill="var(--accent-gray)" x="0" y="24" width="240" height="16"/>
    <path fill="var(--accent-blue)" d="M232 40 V20 Q232 12 240 12 H500 V40 Z"/>
  </svg>
</section>

<section class="card card--back" aria-label="Business card back">
  <div class="brand-name">Ambergate<br>Capital</div>
</section>

</body>
</html>
```